Sorvelle Hearing Health Care Mission

Create a one page flyer (dimensions = 12" wide x 8" tall) that will be turned into a sticker for laptops that highlights our mission statement and our Why, How, and What (elements of the Golden Circle). Additional design direction and content is provided in the attached files.

```html
<!DOCTYPE html>
<html lang="en">
<head>
<meta charset="utf-8">
<title>Sorvelle Hearing Health Care Mission</title>
<link rel="stylesheet" href="https://fonts.googleapis.com/css2?family=Open+Sans:wght@400;600;700;800&display=swap">
<style>
  :root {
    --crimson: #d0213f;
    --orange: #ef5a2a;
    --yellow: #fbb817;
    --purple: #4a1a5c;
    --ink: #444446;
    --muted: #4d4d4f;
    --line: #b9b9bb;
    --paper: #f5f6f7;
    --backdrop: #e4e4e6;
  }
  * { box-sizing: border-box; margin: 0; padding: 0; }
  html, body {
    width: 1200px; height: 910px; overflow: hidden;
    background: var(--backdrop);
    font-family: "Open Sans", Arial, sans-serif;
  }
  .flyer {
    position: absolute; left: 0; top: 55px;
    width: 1200px; height: 800px;
    background: var(--paper);
  }
  .mission-title {
    position: absolute; top: 80px; left: 0; width: 100%;
    text-align: center; font-size: 28px; font-weight: 700;
    color: var(--crimson); letter-spacing: 0.2px;
  }
  .mission-text {
    position: absolute; top: 136px; left: 38px; width: 1124px;
    text-align: center; font-size: 18.5px; line-height: 26px;
    color: var(--ink);
  }
  .golden-circle {
    position: absolute; left: 0; top: 0; width: 1200px; height: 800px;
  }
  .pill {
    position: absolute; left: 444px; width: 351px;
    border-radius: 26px; color: #fff;
    font-weight: 700; font-size: 18px; line-height: 22px;
    display: flex; align-items: center; justify-content: center;
    text-align: center;
  }
  .pill--how { top: 315px; height: 50px; background: var(--orange); }
  .pill--why { top: 442px; height: 53px; background: var(--crimson); font-size: 17.5px; line-height: 21px; }
  .pill--what { top: 571px; height: 51px; background: var(--yellow); }
  .ring-note {
    position: absolute; left: 831px; width: 338px;
  }
  .ring-note h2 {
    font-size: 18px; font-weight: 700; line-height: 22px;
  }
  .ring-note p {
    font-size: 13.6px; line-height: 19.5px; color: var(--muted);
    text-align: justify;
  }
  .ring-note--how { top: 313px; }
  .ring-note--how h2 { color: var(--orange); }
  .ring-note--why { top: 440px; }
  .ring-note--why h2 { color: var(--crimson); }
  .ring-note--what { top: 569px; }
  .ring-note--what h2 { color: var(--yellow); }
  .footer-band {
    position: absolute; left: 31px; top: 733px; width: 1145px; height: 7px;
    background: linear-gradient(90deg, var(--purple), var(--crimson));
  }
  .brand-name {
    position: absolute; right: 24px; top: 747px;
    font-size: 16px; font-weight: 400; color: var(--ink);
    letter-spacing: 0.5px;
  }
</style>
</head>
<body>
  <main class="flyer">
    <h1 class="mission-title">MISSION STATEMENT</h1>
    <p class="mission-text">Hearing health care is complicated. We make it easy by connecting organizations and their customers with quality care, superior products, and an exceptional service experience. Because we believe that everyone deserves to hear well and live happy.</p>

    <svg class="golden-circle" viewBox="0 0 1200 800" aria-hidden="true">
      <circle cx="189" cy="468" r="165" fill="var(--yellow)"/>
      <circle cx="189" cy="468" r="129" fill="var(--orange)" stroke="#fff" stroke-width="2"/>
      <circle cx="189" cy="468" r="82" fill="var(--crimson)" stroke="#fff" stroke-width="2"/>
      <text x="189" y="483" text-anchor="middle" font-family="Open Sans, Arial, sans-serif" font-weight="700" font-size="42" fill="#fff">WHY?</text>
      <g stroke="var(--line)" stroke-width="1.6" fill="none">
        <polyline points="261,393 340,339 444,339"/>
        <polyline points="261,468 444,468"/>
        <polyline points="299,565 340,596 444,596"/>
      </g>
      <g fill="#c9c9cb" stroke="#fff" stroke-width="1.5">
        <circle cx="261" cy="393" r="5"/>
        <circle cx="261" cy="468" r="5"/>
        <circle cx="299" cy="565" r="5"/>
      </g>
    </svg>

    <div class="pill pill--how">How Do You Do / What You Do?</div>
    <div class="pill pill--why">Why Do You Do What You Do?<br>What’s the purpose?</div>
    <div class="pill pill--what">What Do You Do?</div>

    <section class="ring-note ring-note--how">
      <h2>Our How:</h2>
      <p>We make hearing health care simple. We help people navigate the hearing health care journey. We deliver more value.</p>
    </section>
    <section class="ring-note ring-note--why">
      <h2>Our Why:</h2>
      <p>We connect people and resources to improve the lives of people affected by hearing loss.</p>
    </section>
    <section class="ring-note ring-note--what">
      <h2>OurWhat:</h2>
      <p>We partner with organizations to deliver hearing benefits to their customers.</p>
    </section>

    <div class="footer-band"></div>
    <div class="brand-name">Sorvelle</div>
  </main>
</body>
</html>
```